6 Page Brochure for Car Dealers

1. We are an an accident management company in Sydney. Our website is wheelfix.com.au. We provide services for car dealers.

2. We need a 6 page brochure which we can leave with car dealers after we visit them. An example of what we are after is at :
http://www.layoutnest.com/wp-content/uploads/2014/02/Zo-Trend-Auto-Shine-brochure-1.jpg
http://www.layoutnest.com/wp-content/uploads/2014/02/Zo-Trend-Auto-Shine-brochure-3.jpg

3. The layout of the brochure is proposed as follows:

Page 1 - Title page with our logo, visual representation of a happy car dealer, and call to action such as "Try accident management to supercharge profits"

Page 2 - Qualifier page - compares a successful dealership vs an unsuccessful dealership...need a comparison layout similar to this:

https://img-store-bx3.snapboardia.com/736x/a1/42/93/a1429375bd2e6c1047fa3b815ec2d7a9.jpg

Page 3 - Benefits page which shows the customer's journey
Something similar to:

https://www.ridgeservers.com/wp-content/uploads/2015/03/rs-benefits-pdf.png/

Page 4: How to get started page which identifies a four step process: signing agreement, us providing training, reporting accidents using an online portal, collecting payment from us.

Page 5: Testimonials page from other dealerships
Visual logos of our different smash repairer partners

Page 6: Team and contact page with group shot of our whole company, map of where our office is located and office contact details.

Please let us know if you may design something for us.

Target Market(s)

Car dealers

Industry/Entity Type

Car Dealer

Font styles to use
Sans Serif

Colors
f04a50
ec1f27
f59296
fbd4d5

Requirements
Must have
• Please project description
Nice to have

```html
<!DOCTYPE html>
<html lang="en">
<head>
<meta charset="utf-8">
<title>WheelFix Brochure Covers</title>
<link rel="stylesheet" href="https://fonts.googleapis.com/css2?family=Jost:wght@500;700&family=Roboto+Condensed:wght@400;700&display=swap">
<style>
  :root {
    --canvas: #d9d9d9;
    --paper: #ffffff;
    --red: #ec1f27;
    --red-soft: #f04a50;
    --red-deep: #a80d14;
    --red-dark: #7d0a0f;
    --ink: #2b2b2b;
    --white: #ffffff;
  }
  * { box-sizing: border-box; margin: 0; padding: 0; }
  html, body { width: 1200px; height: 1052px; overflow: hidden; }
  body { background: var(--canvas); position: relative; font-family: "Roboto Condensed", sans-serif; }
  .page {
    position: absolute; width: 680px; height: 486px; background: var(--paper);
    box-shadow: 0 8px 22px rgba(0,0,0,.25); overflow: hidden;
  }
  .page svg.art { position: absolute; inset: 0; }
  .back-cover { left: 60px; top: 30px; }
  .front-cover { left: 460px; top: 536px; }

  .contact-list { position: absolute; left: 34px; top: 30px; list-style: none; color: var(--ink); font-size: 14px; line-height: 1.25; text-transform: uppercase; }
  .contact-list li { display: flex; gap: 10px; align-items: flex-start; margin-bottom: 8px; }
  .contact-list svg { flex: none; margin-top: 1px; }

  .call-us { position: absolute; color: var(--white); font-weight: 700; font-size: 19px; line-height: 1.2; text-align: right; text-transform: uppercase; }
  .back-cover .call-us { right: 30px; top: 178px; }
  .front-cover .call-us { right: 34px; top: 285px; font-family: "Roboto Condensed", sans-serif; }

  .phone-list { position: absolute; left: 450px; top: 262px; list-style: none; color: var(--ink); font-size: 16px; }
  .phone-list li { display: flex; align-items: center; gap: 10px; margin-bottom: 10px; }

  .headline { position: absolute; left: 40px; top: 262px; width: 400px; color: var(--white); font-family: "Jost", sans-serif; font-weight: 700; font-size: 26px; line-height: 1.2; letter-spacing: .5px; text-transform: uppercase; }

  .brand { position: absolute; left: 40px; top: 418px; display: flex; align-items: center; gap: 10px; }
  .brand-dot { width: 14px; height: 14px; border-radius: 50%; background: var(--red); }
  .brand-name { font-family: "Jost", sans-serif; font-weight: 700; font-size: 32px; color: var(--red-dark); }
</style>
</head>
<body>

<section class="page back-cover" aria-label="Back cover">
  <svg class="art" width="680" height="486" viewBox="0 0 680 486">
    <defs>
      <linearGradient id="greyPhoto" x1="0" y1="0" x2="0" y2="1">
        <stop offset="0" stop-color="#5a5a5a"/>
        <stop offset=".45" stop-color="#9a9a9a"/>
        <stop offset=".7" stop-color="#4a4a4a"/>
        <stop offset="1" stop-color="#7b7b7b"/>
      </linearGradient>
      <linearGradient id="redSweep" x1="0" y1="0" x2="1" y2="1">
        <stop offset="0" stop-color="var(--red)"/>
        <stop offset="1" stop-color="var(--red-deep)"/>
      </linearGradient>
    </defs>
    <polygon points="400,0 680,0 680,290 520,210" fill="url(#redSweep)"/>
    <polygon points="0,130 680,470 680,486 0,486" fill="url(#greyPhoto)" role="img" aria-label="Black and white photo of a silver sports car on a country road under a cloudy sky"/>
    <polygon points="0,112 680,452 680,470 0,130" fill="var(--red)"/>
    <polygon points="0,330 480,486 0,486" fill="url(#redSweep)"/>
  </svg>

  <ul class="contact-list">
    <li>
      <svg width="12" height="16" viewBox="0 0 12 16"><path d="M6 0a6 6 0 0 0-6 6c0 4.5 6 10 6 10s6-5.5 6-10a6 6 0 0 0-6-6zm0 8.5A2.5 2.5 0 1 1 6 3.5a2.5 2.5 0 0 1 0 5z" fill="var(--red)"/></svg>
      <span>Suite 12, Lv 3, 88 Harbourline St Sydney<br>PO Box 40917 Market Square NSW 2000</span>
    </li>
    <li>
      <svg width="16" height="12" viewBox="0 0 16 12"><rect width="16" height="12" rx="1" fill="var(--red)"/><path d="M0 1l8 6 8-6" stroke="#fff" stroke-width="1.4" fill="none"/></svg>
      <span>contact@wheelfix.com.au</span>
    </li>
  </ul>

  <p class="call-us">Call us :<br>1300 FIXIT 1</p>

  <ul class="phone-list">
    <li>
      <svg width="16" height="16" viewBox="0 0 16 16"><rect x="4" y="1" width="8" height="5" fill="var(--red)"/><rect x="1" y="6" width="14" height="6" rx="1" fill="var(--red)"/><rect x="4" y="10" width="8" height="5" fill="var(--red)" stroke="#fff" stroke-width="1"/></svg>
      <span>02 5550 1842</span>
    </li>
    <li>
      <svg width="16" height="16" viewBox="0 0 16 16"><path d="M3.5 1l3 3-2 2c1 2 3 4 5 5l2-2 3 3-2.5 2.5C7 14 2 9 1 3.5z" fill="var(--red)"/></svg>
      <span>1300 555 913</span>
    </li>
  </ul>
</section>

<section class="page front-cover" aria-label="Front cover">
  <svg class="art" width="680" height="486" viewBox="0 0 680 486">
    <defs>
      <linearGradient id="skyPhoto" x1="0" y1="0" x2="0" y2="1">
        <stop offset="0" stop-color="#7f9bbd"/>
        <stop offset=".45" stop-color="#b8c6d4"/>
        <stop offset=".7" stop-color="#3d454f"/>
        <stop offset="1" stop-color="#2a2f36"/>
      </linearGradient>
      <linearGradient id="bandRed" x1="0" y1="0" x2="1" y2="1">
        <stop offset="0" stop-color="var(--red)"/>
        <stop offset=".6" stop-color="var(--red-deep)"/>
        <stop offset="1" stop-color="var(--red)"/>
      </linearGradient>
    </defs>
    <rect x="0" y="0" width="680" height="240" fill="url(#skyPhoto)" role="img" aria-label="Photo of a dark grey hatchback parked on a road under a blue cloudy sky"/>
    <rect x="0" y="228" width="680" height="150" fill="url(#bandRed)"/>
    <polygon points="0,378 340,378 0,470" fill="var(--paper)"/>
    <polygon points="240,486 680,330 680,486" fill="var(--red)"/>
    <polygon points="420,486 680,400 680,486" fill="var(--red-deep)"/>
  </svg>

  <h1 class="headline">Try accident management to supercharge profits</h1>
  <p class="call-us">Call us :<br>1300 FIXIT 1</p>

  <div class="brand">
    <span class="brand-dot"></span>
    <span class="brand-name">WheelFix</span>
  </div>
</section>

</body>
</html>
```